Seven Rising Steps - Site signage graphic

I need a large board creating to show our Seven Bright Paths plan.

I have added a previous version of this called Seven Bold Moves as well as the draft (AI) version of Seven Rising Steps and our new PowerPoint as an example of branding .

Target Market(s)

Colleagues and visitors to site

Industry/Entity Type

Food manufacturing

Font styles to use
Other font styles liked:
• Raleway Medium

Requirements
Must have
• Clear and all text as per AI mock up

```html
<!DOCTYPE html>
<html lang="en">
<head>
<meta charset="utf-8">
<title>Seven Bright Paths – Site Signage</title>
<link href="https://fonts.googleapis.com/css2?family=Oswald:wght@600;700&family=Raleway:wght@500;700;800&family=Caveat:wght@500&display=swap" rel="stylesheet">
<style>
  :root{
    --green:#00503a;
    --orange:#ec7a24;
    --cream:#f6f2ea;
    --page:#e7e4dd;
    --ink:#1f2a25;
    --green-deco:#2f7058;
    --orange-deco:#f6a623;
    --white:#ffffff;
  }
  *{box-sizing:border-box;margin:0;padding:0}
  html,body{width:873px;height:1200px;overflow:hidden;background:var(--page)}
  .board{
    position:absolute;left:0;top:327px;width:873px;height:545px;
    background:var(--cream);overflow:hidden;
    font-family:"Raleway",sans-serif;color:var(--ink);
  }
  .headline{
    position:absolute;left:29px;top:40px;
    font-family:"Oswald",sans-serif;font-weight:700;color:var(--green);
    font-size:32px;line-height:31px;text-transform:uppercase;letter-spacing:.2px;
  }
  .headline .plan{display:block;margin-top:14px;font-size:35px;line-height:35px}
  .rule-orange{position:absolute;left:87px;top:282px;width:125px;height:1.5px;background:var(--orange)}
  .tagline{position:absolute;left:34px;top:299px;font-size:15px;font-weight:500;color:var(--green)}
  .tagline-script{position:absolute;left:33px;top:318px;font-family:"Caveat",cursive;font-size:21px;color:var(--orange);letter-spacing:.6px}
  .farm-scene{
    position:absolute;left:18px;top:360px;width:231px;height:76px;border-radius:4px;
    background:linear-gradient(180deg,#f1ede4 0%,#dfe6dc 55%,#c9d8cb 100%);
  }
  .rule-dark{position:absolute;left:30px;top:448px;width:211px;height:1px;background:var(--ink)}
  .strap{position:absolute;left:30px;top:459px;width:211px;text-align:center;font-weight:800;font-size:11px;line-height:15px}
  .strap .a{color:var(--green)}
  .strap .b{color:var(--orange)}

  .priority{position:absolute;left:262px;width:611px;height:93px}
  .priority .num{
    position:absolute;left:0;top:-6px;width:46px;text-align:center;
    font-family:"Oswald",sans-serif;font-weight:700;font-size:96px;line-height:105px;
  }
  .priority .band{
    position:absolute;left:46px;top:0;width:565px;height:93px;border-radius:22px 0 0 22px;
  }
  .priority .badge{
    position:absolute;left:66px;top:5.5px;width:82px;height:82px;border-radius:50%;
    background:var(--cream);display:flex;align-items:center;justify-content:center;
  }
  .priority .badge svg{width:50px;height:50px}
  .priority .copy{
    position:absolute;left:164px;top:0;height:93px;width:350px;
    display:flex;flex-direction:column;justify-content:center;
  }
  .copy h2{font-weight:800;font-size:18.5px;line-height:19px;color:var(--white);letter-spacing:-.2px;white-space:nowrap}
  .copy h3{font-weight:800;font-size:13.5px;line-height:17px;white-space:nowrap;letter-spacing:-.2px}
  .copy p{font-weight:500;font-size:10px;line-height:12.2px;color:var(--white);width:290px}
  .priority .deco{position:absolute;right:10px;top:8px;width:80px;height:78px}

  .is-green .num{color:var(--green)}
  .is-green .band{background:var(--green)}
  .is-green .badge{color:var(--green)}
  .is-green h3{color:var(--orange)}
  .is-green .deco{color:var(--green-deco)}
  .is-orange .num{color:var(--orange)}
  .is-orange .band{background:var(--orange)}
  .is-orange .badge{color:var(--orange)}
  .is-orange h3{color:var(--green)}
  .is-orange .deco{color:var(--orange-deco)}

  .p1{top:13px}.p2{top:114px}.p3{top:215px}.p4{top:315px}.p5{top:417px}

  .signoff{
    position:absolute;left:200px;top:517px;font-weight:800;font-size:12px;color:var(--green);
    display:flex;align-items:center;gap:12px;white-space:nowrap;
  }
  .signoff .bar{color:var(--orange);font-weight:500}
  .signoff .script{font-family:"Caveat",cursive;font-weight:500;font-size:17px;color:var(--orange);letter-spacing:.6px;border-bottom:1px solid var(--ink);line-height:15px;padding-bottom:1px}
  svg .s{fill:none;stroke:currentColor;stroke-width:2;stroke-linecap:round;stroke-linejoin:round}
</style>
</head>
<body>
<svg width="0" height="0" style="position:absolute" aria-hidden="true">
  <defs>
    <symbol id="icon-people-plant" viewBox="0 0 48 48"><g class="s">
      <circle cx="15" cy="10" r="4"/><circle cx="24" cy="7" r="4.5"/><circle cx="33" cy="10" r="4"/>
      <path d="M8 24c0-5 3-8 7-8M40 24c0-5-3-8-7-8M16 22c0-6 4-9 8-9s8 3 8 9"/>
      <path d="M24 44V26M24 34c-7 0-10-4-10-9 6 0 10 3 10 9M24 31c6 0 10-4 10-9-6 0-10 3-10 9"/>
    </g></symbol>
    <symbol id="icon-shield-lock" viewBox="0 0 48 48"><g class="s">
      <path d="M24 4l16 6v11c0 11-7 18-16 23C15 39 8 32 8 21V10z"/>
      <path d="M24 8l12 4.5V21c0 8-5 14-12 18-7-4-12-10-12-18v-8.5z"/>
      <rect x="18" y="22" width="12" height="10" rx="1.5"/><path d="M20 22v-3a4 4 0 0 1 8 0v3M24 26v2"/>
    </g></symbol>
    <symbol id="icon-rosette" viewBox="0 0 48 48"><g class="s">
      <path d="M24 3l4 3 5-1 2 4.5 4.5 2-1 5 3 4-3 4 1 5-4.5 2-2 4.5-5-1-4 3-4-3-5 1-2-4.5-4.5-2 1-5-3-4 3-4-1-5 4.5-2 2-4.5 5 1z"/>
      <circle cx="24" cy="20.5" r="9"/>
      <path d="M24 15l1.8 3.7 4 .5-3 2.8.8 4-3.6-2-3.6 2 .8-4-3-2.8 4-.5z"/>
      <path d="M16 34l-5 11 5-2 3 4 4-10M32 34l5 11-5-2-3 4-4-10"/>
    </g></symbol>
    <symbol id="icon-group" viewBox="0 0 48 48"><g class="s">
      <circle cx="12" cy="17" r="4.5"/><circle cx="24" cy="13" r="5.5"/><circle cx="36" cy="17" r="4.5"/>
      <path d="M3 34c0-6 4-10 9-10 2 0 3 .4 4 1M45 34c0-6-4-10-9-10-2 0-3 .4-4 1"/>
      <path d="M13 36c0-8 5-14 11-14s11 6 11 14z M3 34h10M35 34h10"/>
    </g></symbol>
    <symbol id="icon-bulb" viewBox="0 0 48 48"><g class="s">
      <path d="M17 31c-3-3-5-6-5-10a12 12 0 0 1 24 0c0 4-2 7-5 10v4H17z"/>
      <path d="M18 39h12M20 43h8M21 31l-2-9 5 3 5-3-2 9"/>
      <path d="M24 2v3M8 8l2 2M40 8l-2 2M3 21h3M42 21h3"/>
    </g></symbol>
    <symbol id="deco-globe-leaf" viewBox="0 0 48 48"><g class="s" stroke-width="1.6">
      <circle cx="24" cy="24" r="20"/>
      <path d="M8 16c5 1 6 5 10 5s3 6 7 7M28 4c-2 4 1 6 4 7s3 5 8 5"/>
      <path d="M26 44c0-12 6-20 18-22 0 12-6 20-18 22zM28 41l12-15"/>
    </g></symbol>
    <symbol id="deco-shield-circuit" viewBox="0 0 48 48"><g class="s" stroke-width="1.6">
      <path d="M24 4l13 5v10c0 10-6 17-13 21-7-4-13-11-13-21V9z"/>
      <path d="M24 8l9 3.5V19c0 7-4 12-9 15-5-3-9-8-9-15v-7.5z"/>
      <rect x="19" y="19" width="10" height="9" rx="1"/><path d="M21 19v-3a3 3 0 0 1 6 0v3"/>
      <path d="M11 17H6l-2-2M11 25H3M12 31H7l-2 2M37 17h5l2-2M37 25h8M36 31h5l2 2"/>
      <circle cx="3" cy="14" r="1.5"/><circle cx="2" cy="25" r="1.5"/><circle cx="4" cy="34" r="1.5"/>
      <circle cx="45" cy="14" r="1.5"/><circle cx="46" cy="25" r="1.5"/><circle cx="44" cy="34" r="1.5"/>
    </g></symbol>
    <symbol id="deco-handshake" viewBox="0 0 48 48"><g class="s" stroke-width="1.6">
      <path d="M2 14l7-2 5 18-7 2zM46 14l-7-2-5 18 7 2z"/>
      <path d="M12 15l8-3 6 2 6-2 7 3M35 28l-8 7c-1 1-3 1-4 0M31 25l-8 7c-1 1-3 1-4 0M28 22l-7 6c-1 1-3 1-4 0l-3-3"/>
      <path d="M26 14l-7 5c-1 1-1 3 1 3 2 1 4 0 6-2l3-2 6 8"/>
    </g></symbol>
    <symbol id="deco-bulb-gear" viewBox="0 0 48 48"><g class="s" stroke-width="1.6">
      <path d="M16 32c-3-3-5-6-5-11a13 13 0 0 1 26 0c0 5-2 8-5 11v4H16z"/>
      <path d="M17 40h14M20 44h8M24 1v3M7 6l2 2M41 6l-2 2M2 21h3M43 21h3"/>
      <circle cx="24" cy="21" r="4"/>
      <path d="M24 13v3M24 26v3M16 21h3M29 21h3M18.5 15.5l2 2M27.5 24.5l2 2M29.5 15.5l-2 2M20.5 24.5l-2 2"/>
    </g></symbol>
  </defs>
</svg>

<main class="board">
  <h1 class="headline">From<br>Cheesemakers<br>to<br>Changemakers:<span class="plan">Seven Bright<br>Paths</span></h1>
  <div class="rule-orange"></div>
  <p class="tagline">Proud of our heritage.</p>
  <p class="tagline-script">Focused on our future.</p>
  <div class="farm-scene" role="img" aria-label="Line illustration of a farmstead with barns, trees and grazing cows"></div>
  <div class="rule-dark"></div>
  <p class="strap"><span class="a">FROM FARM TO FORK.</span><br><span class="b">WE'RE SHAPING THE INDUSTRY.</span></p>

  <section class="priority is-green p1">
    <div class="num">1</div><div class="band"></div>
    <div class="badge"><svg><use href="#icon-people-plant"/></svg></div>
    <div class="copy">
      <h2>PEOPLE, PLACES &amp; PRODUCTS</h2>
      <h3>WE DO THINGS THE RIGHT WAY</h3>
      <p>Our success starts with great people, strong communities and quality milk. We are committed to producing food responsibly, supporting our farming partners and creating opportunities for future generations.</p>
    </div>
    <svg class="deco"><use href="#deco-globe-leaf"/></svg>
  </section>

  <section class="priority is-orange p2">
    <div class="num">2</div><div class="band"></div>
    <div class="badge"><svg><use href="#icon-shield-lock"/></svg></div>
    <div class="copy">
      <h2>CYBER SECURITY</h2>
      <h3>PROTECTING WHAT MATTERS</h3>
      <p>Every colleague plays a role in keeping our information, systems and customers safe. Strong cyber security protects our business today and supports our future growth.</p>
    </div>
    <svg class="deco"><use href="#deco-shield-circuit"/></svg>
  </section>

  <section class="priority is-green p3">
    <div class="num">3</div><div class="band"></div>
    <div class="badge"><svg><use href="#icon-rosette"/></svg></div>
    <div class="copy">
      <h2>QUALITY &amp; CONTINUOUS IMPROVEMENT</h2>
      <h3>BE THE BEST AT WHAT WE DO</h3>
      <p>Quality and food safety are at the heart of everything we do. By continually improving our processes, reducing waste and learning every day, we deliver products our customers can trust.</p>
    </div>
    <svg class="deco"><use href="#icon-rosette"/></svg>
  </section>

  <section class="priority is-orange p4">
    <div class="num">4</div><div class="band"></div>
    <div class="badge"><svg><use href="#icon-group"/></svg></div>
    <div class="copy">
      <h2>CUSTOMER FOCUS</h2>
      <h3>BUILD TRUST. CREATE VALUE. FOR THE LONG TERM.</h3>
      <p>We build strong, long-term relationships based on trust by understanding our customers' needs and working together to deliver outstanding value.</p>
    </div>
    <svg class="deco"><use href="#deco-handshake"/></svg>
  </section>

  <section class="priority is-green p5">
    <div class="num">5</div><div class="band"></div>
    <div class="badge"><svg><use href="#icon-bulb"/></svg></div>
    <div class="copy">
      <h2>TRANSFORMATION &amp; INNOVATION</h2>
      <h3>SHAPING TOMORROW, TODAY</h3>
      <p>We challenge ourselves to think differently, embrace change and never stand still. Through innovation, collaboration and continuous improvement, we will build a stronger, smarter and more sustainable Brookvale Foods for the future.</p>
    </div>
    <svg class="deco"><use href="#deco-bulb-gear"/></svg>
  </section>

  <footer class="signoff">
    <span>ONE BUSINESS. ONE PURPOSE. FIVE PRIORITIES.</span>
    <span class="bar">|</span>
    <span class="script">Let's thrive together.</span>
  </footer>
</main>
</body>
</html>
```